Sleek, Professional Business Card Design Needed

Business Cards - Logo Attached.

We are a solar consulting company. We are national and want our cards to represent the professional high quality products that we offer.

Industry/Entity Type

Business

Contact Information for Business Card

n/a

Requirements
Must have
• Design
• Name
• Position
• Number
• Email
• Address
Should not have
• Not be too crowded

```html
<!DOCTYPE html>
<html lang="en">
<head>
<meta charset="utf-8">
<title>Brightfield Solar – Business Card</title>
<link rel="stylesheet" href="https://fonts.googleapis.com/css2?family=Roboto:wght@400;500;700&display=swap">
<style>
  :root {
    --page-bg: #e4e4e4;
    --card-white: #f4f4f3;
    --brand-green: #5cab38;
    --brand-teal: #17958f;
    --brand-blue: #1479b8;
    --accent-blue: #1a8bd6;
    --text-dark: #2b2b2b;
    --text-white: #ffffff;
  }
  * { margin: 0; padding: 0; box-sizing: border-box; }
  html, body {
    width: 1200px; height: 576px; overflow: hidden;
    background: var(--page-bg);
    font-family: "Roboto", Arial, sans-serif;
  }
  .canvas { position: relative; width: 1200px; height: 576px; }

  .card {
    position: absolute; top: 138px;
    width: 484px; height: 294px;
    border-radius: 14px; overflow: hidden;
    box-shadow: 0 3px 6px rgba(0,0,0,0.18);
  }

  /* Front side */
  .card-front {
    left: 82px;
    background: linear-gradient(180deg, var(--brand-green) 0%, var(--brand-teal) 55%, var(--brand-blue) 100%);
    display: flex; flex-direction: column; align-items: center; justify-content: center;
    gap: 16px;
  }
  .front-mark {
    width: 84px; height: 84px; border-radius: 50%;
    border: 7px solid var(--text-white);
  }
  .front-name {
    color: var(--text-white);
    font-weight: 500; font-size: 30px; letter-spacing: 0.5px;
    text-transform: uppercase; white-space: nowrap;
  }

  /* Back side */
  .card-back { left: 602px; background: var(--card-white); }
  .back-ring { position: absolute; left: 232px; top: 0; }
  .back-brand {
    position: absolute; left: 18px; top: 34px;
    color: var(--accent-blue);
    font-weight: 500; font-size: 19px; letter-spacing: 0;
    text-transform: uppercase; white-space: nowrap;
  }
  .person-name {
    position: absolute; left: 18px; top: 130px;
    color: var(--accent-blue); font-weight: 700; font-size: 21px;
  }
  .person-role {
    position: absolute; left: 18px; top: 158px;
    color: var(--text-dark); font-size: 12px;
  }
  .contact-list {
    position: absolute; left: 18px; top: 200px;
    list-style: none; color: var(--text-dark); font-size: 12.5px;
  }
  .contact-list li { display: flex; align-items: center; height: 18.5px; white-space: nowrap; }
  .contact-list svg { width: 11px; height: 11px; margin-right: 10px; fill: var(--accent-blue); }
  .contact-list .address { margin-top: 2px; }
  .web-domain { color: var(--accent-blue); }
</style>
</head>
<body>
<main class="canvas">
  <section class="card card-front">
    <div class="front-mark"></div>
    <div class="front-name">Brightfield Solar</div>
  </section>

  <section class="card card-back">
    <svg class="back-ring" width="280" height="294" viewBox="0 0 280 294">
      <circle cx="136" cy="148" r="134" fill="none" stroke="var(--accent-blue)" stroke-width="14"/>
    </svg>
    <div class="back-brand">Brightfield Solar</div>
    <h1 class="person-name">Daniel Carter</h1>
    <p class="person-role">Managing Director</p>
    <ul class="contact-list">
      <li>
        <svg viewBox="0 0 24 24"><path d="M3 8c0-3 4-5 9-5s9 2 9 5v2h-5V8H8v2H3zM6 11h12l3 10H3z"/></svg>
        1800-555-0142
      </li>
      <li>
        <svg viewBox="0 0 24 24"><path d="M2 5h20v14H2zM3 6l9 7 9-7v2l-9 7-9-7z" fill-rule="evenodd"/></svg>
        dcarter@brightfield.com
      </li>
      <li>
        <svg viewBox="0 0 24 24"><circle cx="12" cy="12" r="10"/></svg>
        <span>www.<span class="web-domain">brightfieldsolar</span>.com</span>
      </li>
      <li class="address">48, Harbor Lane No, Country 456</li>
    </ul>
  </section>
</main>
</body>
</html>
```